AUSTRALIAN CONSULTING FIRM BUSINESS CARD - MODERN

We are wanting a modern, clean lined business card design. We are professional niche consultancy firm situated in Australia called Harbrook Advisory Partners Pty Ltd.
The card should communicate professionalism and creativity and draw on our logo design (attached).
The design should be two sided, landscape orientation.
Target Market(s)
government, not for profit sector, corporate clients
Industry/Entity Type
Landscape
Requirements
Must have
- logo
no new introduced colours

```html
<!DOCTYPE html>
<html lang="en">
<head>
<meta charset="utf-8">
<title>Harbrook Advisory Partners – Business Card</title>
<link rel="stylesheet" href="https://fonts.googleapis.com/css2?family=Cabin:wght@400;600;700&display=swap">
<style>
  :root {
    --bg: #2a2a2a;
    --green-light: #a8d118;
    --green-dark: #2f9a2c;
    --navy: #1d3f8f;
    --purple: #9b1a7e;
    --purple-dark: #7d1466;
    --ink: #333333;
    --muted: #555555;
    --paper: #ffffff;
    --paper-shade: #e9e9e9;
  }
  * { margin: 0; padding: 0; box-sizing: border-box; }
  html, body {
    width: 1200px; height: 901px; overflow: hidden;
    background: var(--bg);
    font-family: "Cabin", sans-serif;
  }
  .stage {
    width: 1200px; height: 901px;
    display: flex; flex-direction: column;
    align-items: center; justify-content: center; gap: 56px;
  }
  .card {
    position: relative;
    width: 620px; height: 354px;
    border-radius: 22px;
    overflow: hidden;
  }
  /* Back side */
  .card--back {
    background: linear-gradient(135deg, var(--green-light) 0%, var(--green-dark) 100%);
    display: flex; align-items: center; justify-content: center;
  }
  .brand {
    display: flex; align-items: center; gap: 14px;
  }
  .brand__dot {
    width: 34px; height: 34px; border-radius: 50%;
    background: var(--navy);
    flex: none;
  }
  .brand__name {
    font-weight: 700;
    color: var(--navy);
    text-transform: uppercase;
    line-height: 1.05;
  }
  .card--back .brand__name { font-size: 26px; }
  /* Front side */
  .card--front {
    background: linear-gradient(180deg, var(--paper) 0%, var(--paper) 70%, var(--paper-shade) 100%);
  }
  .card--front .brand {
    position: absolute; left: 40px; top: 38px;
  }
  .card--front .brand__dot { width: 28px; height: 28px; }
  .card--front .brand__name { font-size: 19px; }
  .contact {
    position: absolute; left: 150px; top: 134px;
  }
  .contact__name {
    font-size: 24px; color: var(--navy); font-weight: 400;
    letter-spacing: 0.5px; text-transform: uppercase;
  }
  .contact__role {
    font-size: 15px; color: var(--ink); margin-top: 2px;
  }
  .contact__list {
    margin-top: 22px;
    display: grid; grid-template-columns: 52px auto; row-gap: 4px;
    font-size: 15px;
  }
  .contact__label { color: var(--purple); font-weight: 600; }
  .contact__value { color: var(--ink); }
  .address-band {
    position: absolute; left: 0; right: 0; bottom: 0; height: 52px;
    background: linear-gradient(180deg, var(--purple) 0%, var(--purple-dark) 100%);
    display: flex; align-items: center; justify-content: center;
    color: #f3dcec; font-size: 16px; letter-spacing: 0.3px;
  }
</style>
</head>
<body>
  <main class="stage">
    <section class="card card--back" aria-label="Card back">
      <div class="brand">
        <span class="brand__dot"></span>
        <span class="brand__name">Harbrook Advisory<br>Partners Pty Ltd</span>
      </div>
    </section>

    <section class="card card--front" aria-label="Card front">
      <div class="brand">
        <span class="brand__dot"></span>
        <span class="brand__name">Harbrook Advisory<br>Partners Pty Ltd</span>
      </div>
      <div class="contact">
        <h1 class="contact__name">Daniel Whitmore</h1>
        <p class="contact__role">managing director</p>
        <dl class="contact__list">
          <dt class="contact__label">phone</dt><dd class="contact__value">02 9123 4567</dd>
          <dt class="contact__label">cell</dt><dd class="contact__value">0412 345 678</dd>
          <dt class="contact__label">email</dt><dd class="contact__value">info@harbrookadvisory.com</dd>
        </dl>
      </div>
      <div class="address-band">48 Wattle Lane, Riverside, NSW 2150</div>
    </section>
  </main>
</body>
</html>
```